Sales Brochure

We require a sales brochure for our outsourced payroll bureau.

Please refer to our logo's attached, design content brief attached and our website www.quillbrook.com.au

We require to brochure to be:

- Professional BUT not stale, boring or over corporate. We want to be seen as being different, modern, fun, easy to work with, simple

Please be aware that the logo's provided are low quality. You will need to replicate the logo in high res for this brochure. Also please note we require to see the brochure layout of the internal pages - not just the front and back

```html
<!DOCTYPE html>
<html lang="en">
<head>
<meta charset="utf-8">
<title>Quillbrook Brochure Cover Spread</title>
<link rel="stylesheet" href="https://fonts.googleapis.com/css2?family=Source+Sans+3:wght@300;400;600&display=swap">
<style>
  :root {
    --page-bg: #e6e6e6;
    --back-paper: #f4f4f4;
    --front-blue: #2d84c1;
    --band-blue: #64a4d9;
    --logo-blue: #5ea3dc;
    --edge-grey: #c9cbcd;
    --ink: #3d3d3d;
    --white: #ffffff;
    --mascot-tone: #ead9cc;
    --photo-light: #dfe5ea;
    --photo-dark: #3e4a5a;
  }
  html, body {
    margin: 0;
    padding: 0;
    width: 1200px;
    height: 844px;
    overflow: hidden;
    background: var(--page-bg);
  }
  .spread {
    display: block;
    width: 1200px;
    height: 844px;
    font-family: "Source Sans 3", "Helvetica Neue", Arial, sans-serif;
  }
  .back-paper { fill: var(--back-paper); }
  .front-panel { fill: var(--front-blue); }
  .band-edge { fill: var(--edge-grey); }
  .back-band { fill: var(--band-blue); }
  .mascot-area { fill: var(--mascot-tone); opacity: 0.6; }
  .brand-name { font-weight: 600; }
  .brand-name--back { fill: var(--logo-blue); font-size: 40px; letter-spacing: 2px; }
  .brand-name--front { fill: var(--white); font-size: 62px; letter-spacing: 3px; }
  .brand-dot--back { fill: var(--logo-blue); }
  .brand-dot--front { fill: var(--white); }
  .contact-title { fill: var(--white); font-size: 22px; font-weight: 400; }
  .contact-line { fill: var(--white); font-size: 12px; font-weight: 400; }
  .contact-line tspan.value { font-weight: 600; }
  .closing-note { fill: var(--ink); font-size: 12px; font-weight: 400; }
  .web-address { fill: var(--white); font-size: 13px; font-weight: 600; letter-spacing: 0.3px; }
  .tagline { fill: var(--white); font-size: 33px; font-weight: 300; }
</style>
</head>
<body>
<svg class="spread" viewBox="0 0 1200 844" xmlns="http://www.w3.org/2000/svg">
  <defs>
    <linearGradient id="officePhotoTone" x1="0" y1="0" x2="1" y2="1">
      <stop offset="0" stop-color="var(--photo-light)"/>
      <stop offset="0.55" stop-color="#c2ccd6"/>
      <stop offset="1" stop-color="var(--photo-dark)"/>
    </linearGradient>
  </defs>

  <g class="back-cover">
    <rect class="back-paper" x="102" y="77" width="514" height="720"/>

    <text class="brand-name brand-name--back" x="345" y="172" text-anchor="middle">quillbrook</text>
    <circle class="brand-dot--back" cx="463" cy="150" r="5"/>

    <rect class="mascot-area" x="276" y="205" width="130" height="108" rx="12"
          role="img" aria-label="Faint cheerful mascot illustration"/>

    <polygon class="band-edge" points="102,424 387,375 387,389 616,349 616,645 330,695 330,681 102,721"/>
    <polygon class="back-band" points="102,431 387,382 387,396 616,356 616,637 330,687 330,673 102,713"/>

    <text class="contact-title" x="360" y="525" text-anchor="middle">CEO: Daniel Whitcombe MBA</text>
    <text class="contact-line" x="360" y="547" text-anchor="middle">Email: <tspan class="value">daniel.w@quillbrook.com.au</tspan></text>
    <text class="contact-line" x="360" y="566" text-anchor="middle">Phone: <tspan class="value">0400 318 265</tspan></text>

    <text class="closing-note" x="362" y="749" text-anchor="middle">Quillbrook would love to hear from with you.</text>
    <text class="closing-note" x="362" y="764" text-anchor="middle">Our team come to you, obligation free, Australia wide.</text>
  </g>

  <g class="front-cover">
    <rect class="front-panel" x="616" y="77" width="514" height="720"/>

    <text class="brand-name brand-name--front" x="860" y="198" text-anchor="middle">quillbrook</text>
    <circle class="brand-dot--front" cx="1040" cy="170" r="6"/>

    <polygon class="band-edge" points="616,346 905,296 905,310 1130,272 1130,567 845,618 845,604 616,646"/>
    <polygon fill="url(#officePhotoTone)" points="616,355 905,305 905,319 1130,281 1130,559 845,610 845,596 616,637"
             role="img" aria-label="Photo of office colleagues reviewing paperwork at a desk with a computer"/>

    <text class="web-address" x="865" y="708" text-anchor="middle">www.quillbrook.com.au</text>
    <text class="tagline" x="865" y="752" text-anchor="middle">get payroll off your back</text>
  </g>
</svg>
</body>
</html>
```